UPDATED BRIEF: Hypermobile EDS Book Cover Contest

I am writing a print book. I need cover designs to evaluate with your creativity. It is a nonfiction memoir meets self-help guide to living with a rare, incurable chronic illness called EDS. See attached Word doc for book details and copy. It is designed to be an inspiration story of living well with this disease so mindset is a key theme. I'm looking for all types of ideas including photography (sailboat, mountain, journey concepts), type flat designs highlighting hypermobility (a key part of the disease), including good use of color and white space. I want it to be legible, intriguing, and emotive if possible. I need someone to be able to produce and provide the production files and/or edit the final text back copy as it is not yet final. I will be sharing the contest with my fan base. I will ultimately need the cover, back cover, spine, and audio and ebook covers done all the same just reformatted to size. Print book 6x9 to be done first. I dont want to provide too much direction so you can be creative.
Updates

I uploaded a new brief for updated author name and back cover. Please update and I will start the poll. I will also extend the project timeline.

Can anyone create a design with the typeset words of hypermobile on the title being "pinched" by a string? Like holding it all together by a string?

Went on vacation/holiday

Target Market(s)

chronic illness disease victims, specifically those with Hypermobile Ehlers Danlos Syndrome (EDS), dysautonomia (POTS) or craniocervical instability in the neck

Industry/Entity Type

Self help, personal development, memoir

Font styles to use
Sans Serif

Colors
FFC000
F8CF3A
FAE287
FDF2CF
FEFAEE

Requirements
Must have
• legible, intriguing even emotive design with text or photos
Nice to have
• Potentially visually showing a journey, hypermobility, or overcoming obstacles
Should not have
• black dark backgrounds

```html
<!DOCTYPE html>
<html lang="en">
<head>
<meta charset="utf-8">
<title>Living Well and Staying Strong While Hypermobile – Book Cover Wrap</title>
<link href="https://fonts.googleapis.com/css2?family=Anton&family=Antonio:wght@400;700&family=Fira+Sans:wght@600&family=Roboto+Condensed:ital,wght@0,300;0,700;1,700&display=swap" rel="stylesheet">
<style>
  :root {
    --page: #fefaee;
    --cover: #f8cf3a;
    --ink: #111111;
    --paper: #f4f2ee;
    --paper-shade: #e6e3dc;
    --shadow: rgba(90, 70, 20, 0.28);
  }
  * { margin: 0; padding: 0; box-sizing: border-box; }
  html, body { width: 1200px; height: 1000px; overflow: hidden; background: var(--page); }
  .canvas { position: relative; width: 1200px; height: 1000px; background: var(--page); }

  .wrap {
    position: absolute; left: 156px; top: 173px; width: 888px; height: 650px;
    background: var(--cover);
    box-shadow: 0 8px 18px var(--shadow);
  }
  .spine { position: absolute; left: 589px; top: 173px; width: 22px; height: 650px; background: var(--ink); }

  .type-layer { position: absolute; left: 0; top: 0; width: 1200px; height: 1000px; pointer-events: none; }
  .t-light { font-family: "Antonio", "Oswald", sans-serif; font-weight: 400; fill: var(--ink); }
  .t-heavy { font-family: "Anton", "Oswald", sans-serif; font-weight: 400; fill: var(--ink); }
  .t-spine { font-family: "Antonio", "Oswald", sans-serif; font-weight: 400; fill: var(--cover); }
  .t-spine .strong { font-weight: 700; }

  .art { position: absolute; }
  .art--back-piece {
    left: 470px; top: 216px; width: 98px; height: 96px;
    background: var(--ink); border-radius: 30% 42% 36% 44%; transform: rotate(-28deg);
  }
  .art--spine-piece { left: 592px; top: 223px; width: 16px; height: 16px; background: var(--cover); border-radius: 3px; }
  .art--head {
    left: 751px; top: 473px; width: 163px; height: 237px;
    background: linear-gradient(180deg, var(--paper) 0%, var(--paper-shade) 100%);
    border-radius: 60px 60px 8px 8px;
  }
  .author-photo {
    position: absolute; left: 181px; top: 718px; width: 66px; height: 81px;
    background: linear-gradient(135deg, #d8492f 0%, #b8321f 60%, #2a1c1a 100%);
  }

  .back-copy {
    position: absolute; left: 180px; width: 385px;
    font-family: "Roboto Condensed", "Arial Narrow", sans-serif;
    font-weight: 300; color: var(--ink);
    font-size: 8.1px; line-height: 11px;
  }
  .back-copy b { font-weight: 700; }
  .back-copy .title-ref { font-weight: 700; font-style: italic; }
  .back-lede { top: 353px; width: 400px; font-size: 12.4px; line-height: 17px; }
  .back-head { top: 412px; font-weight: 700; }
  .back-intro { top: 433px; }
  .back-quote { top: 552px; font-weight: 700; }
  .back-companion { top: 574px; }
  .back-prescription { top: 618px; }
  .back-explores { top: 639px; }
  .back-tools { top: 683px; }
  .back-bio { top: 714px; left: 253px; width: 312px; }
  .back-bio .bio-head { display: block; font-weight: 700; }

  .subtitle {
    position: absolute; left: 611px; top: 392px; width: 433px; text-align: center;
    font-family: "Fira Sans", "Arial", sans-serif; font-weight: 600;
    font-size: 13.2px; line-height: 17px; color: var(--ink); letter-spacing: 0.2px;
  }
</style>
</head>
<body>
<div class="canvas">
  <div class="wrap"></div>
  <div class="spine"></div>

  <div class="art art--back-piece" role="img" aria-label="Photograph of a single black jigsaw puzzle piece on yellow"></div>
  <div class="author-photo" role="img" aria-label="Author portrait photograph against a red background"></div>
  <div class="art art--spine-piece" role="img" aria-label="Small jigsaw puzzle piece emblem"></div>
  <div class="art art--head" role="img" aria-label="Paper cut-out of a head in profile with an open top and a black puzzle piece floating above it"></div>

  <svg class="type-layer" viewBox="0 0 1200 1000" xmlns="http://www.w3.org/2000/svg">
    <!-- back cover -->
    <text class="t-heavy" x="178" y="204" font-size="21" textLength="79" lengthAdjust="spacingAndGlyphs">MAE R. LIND</text>
    <text class="t-light" x="178" y="246" font-size="31" textLength="155" lengthAdjust="spacingAndGlyphs">LIVING WELL AND</text>
    <text class="t-light" x="178" y="279" font-size="31" textLength="243" lengthAdjust="spacingAndGlyphs">STAYING STRONG WHILE</text>
    <text class="t-heavy" x="178" y="333" font-size="52" textLength="245" lengthAdjust="spacingAndGlyphs">HYPERMOBILE</text>

    <!-- spine -->
    <text class="t-spine" transform="translate(606 603) rotate(-90)" font-size="17" textLength="323" lengthAdjust="spacingAndGlyphs">LIVING WELL AND STAYING STRONG WHILE <tspan class="strong">HYPERMOBILE</tspan></text>
    <text class="t-spine" transform="translate(606 791) rotate(-90)" font-size="17" font-weight="700" textLength="73" lengthAdjust="spacingAndGlyphs">MAE R. LIND</text>

    <!-- front cover -->
    <text class="t-light" x="709" y="240" font-size="49" textLength="240" lengthAdjust="spacingAndGlyphs">LIVING WELL AND</text>
    <text class="t-light" x="639" y="293" font-size="48" textLength="378" lengthAdjust="spacingAndGlyphs">STAYING STRONG WHILE</text>
    <text class="t-heavy" x="639" y="377" font-size="82" textLength="378" lengthAdjust="spacingAndGlyphs">HYPERMOBILE</text>
    <text class="t-heavy" x="733" y="800" font-size="47" textLength="188" lengthAdjust="spacingAndGlyphs">MAE R. LIND</text>
  </svg>

  <p class="subtitle">Build a Brighter Daily Life Living with<br>EDS, POTS, and Instability</p>

  <p class="back-copy back-lede">Begin feeling better today with small, steady routines. Turn hurt into hope with this warm, practical guide to help you understand the many layers of <b>hEDS</b>.<br>The road is long, but you never walk it alone.</p>

  <p class="back-copy back-head">The Everyday Guide to Coping and Thriving with Rare Chronic Illness</p>

  <p class="back-copy back-intro">In <span class="title-ref">“Living Well and Staying Strong While Hypermobile,”</span> Marla Lind takes a close look at daily life with hypermobile Ehlers Danlos Syndrome <b>(hEDS)</b>. Learn why <b>hEDS</b> is being recognized more often, and how to ease the hardship on the way to calm and well-being. Inside you will find…<br>
  • Her honest account of building a full and happy life with <b>hEDS</b><br>
  • Conversations with trusted clinicians, patient groups and advocates<br>
  • Reflections, prompts, and sayings to guide your own search for clarity<br>
  • A daily plan for growing a hopeful, resilient outlook.<br>
  <span class="title-ref">“Living Well and Staying Strong While Hypermobile”</span> will help you trust that a painful lifelong condition need not define you. You will also feel better prepared to stand beside the people you care about who live with <b>hEDS</b>, with patience and real understanding.</p>

  <p class="back-copy back-quote">“A trusted companion for anyone living with chronic pain”</p>

  <p class="back-copy back-companion">Whether you or someone close to you has recently learned they have hypermobile Ehlers Danlos Syndrome <b>(hEDS)</b>, this book is a steady guide for the road ahead. Drawing on interviews, clinical insight, and stories from fellow patients, it helps you find clear answers and shape a life that feels good to live.</p>

  <p class="back-copy back-prescription">Discover your own plan for progress and a more hopeful way of thinking!</p>

  <p class="back-copy back-explores">The book explains what lies behind <b>hEDS</b> and shares useful, down-to-earth ideas for building a rich and rewarding life with this rare, lifelong condition. It also looks ahead to new medical research and shows how to keep a hopeful outlook when times are hard.</p>

  <p class="back-copy back-tools">These pages give you what you need to return to work or study, gain assurance from expert medical guidance, and arm yourself with knowledge that can change your days for good.</p>

  <p class="back-copy back-bio"><span class="bio-head">Author Biography</span>Marla Lind has always been bendy and usually cheerful. Only after a proper diagnosis of Ehlers Danlos Syndrome in her late forties did she make sense of her body’s oddities. After many years of puzzling symptoms, she moved from being doubted and overlooked to being resolute, turning her energy into this labor of love for others on a similar path. She lives near a quiet lake with her partner and enjoys long walks outdoors when she isn’t busy with her ongoing work of learning to cope and heal with a rare, lifelong condition.<br>To learn more about Marla and her patient advocacy work, visit <b>www.pathtobrightdays.com.</b></p>
</div>
</body>
</html>
```